Making my choice by 12:00 Noon (Eastern Time) today 9/25/14 Thank you all for participating.

I am working on a present day, Young Adult, fantasy book series. The primary character’s name is Martin Quill; his company, which will be located in the UK is The Lantern Bureau, or The Lantern Bureau. Their tag line will be: Detectives, Solving Supernatural Crimes. This will be book #1 in the series and I would like it identified as such in the cover design.

Title will be: The Lantern Bureau
Sub-title: Detectives, Solving Supernatural Crimes
Author: Howard Blenkin

The film Harbour Fog Cipher Ghost would best sum up the characters, setting, and mood. http://www.harbour-fog-cipher-ghost.example/paralax.htm#research

The spine size is "to be determined" at this point as the overall word count is not in. We can, however, safely assume that it will not be less than 50,000 words using a 5 inch x 8 inch book size - 50K words, 200 pages, 50# offset, Spine Width is approx. 0.391 inches.

The book will be both eBook format and print on demand paperback from Bookvane. Thanks, Howard

Young Adult

Adult

Serif

• Book #1

```html
<!DOCTYPE html>
<html lang="en">
<head>
<meta charset="utf-8">
<title>The Lantern Bureau — Book #1 Cover</title>
<link rel="stylesheet" href="https://fonts.googleapis.com/css2?family=Barlow:wght@600;700&family=Barlow+Condensed:wght@400;600;700&display=swap">
<style>
  :root {
    --backdrop: #8f8279;
    --leather-deep: #1f0f08;
    --leather-mid: #3a1d10;
    --leather-glow: #5a3020;
    --gold: #d9a97c;
    --gold-dark: #8a5a38;
    --band: #ffffff;
    --band-rule: #b9b9b9;
    --ink: #111111;
    --book-ink: #4a2612;
  }
  * { margin: 0; padding: 0; box-sizing: border-box; }
  html, body {
    width: 1200px;
    height: 1200px;
    overflow: hidden;
    background: var(--backdrop);
  }
  .cover {
    position: absolute;
    left: 288px;
    top: 100px;
    width: 624px;
    height: 1000px;
    background: var(--leather-deep);
    overflow: hidden;
  }
  .cover__leather {
    position: absolute;
    inset: 0 0 134px 0;
    background:
      radial-gradient(ellipse 70% 40% at 70% 30%, rgba(120,70,45,0.45), transparent 70%),
      linear-gradient(160deg, var(--leather-mid) 0%, var(--leather-deep) 45%, var(--leather-glow) 60%, var(--leather-deep) 78%, #170a05 100%);
  }
  .title {
    position: absolute;
    left: 0;
    right: 0;
    top: 250px;
    text-align: center;
    font-family: "Barlow Condensed", sans-serif;
    color: var(--gold);
  }
  .title__article {
    font-weight: 700;
    font-size: 40px;
    letter-spacing: 2px;
    margin-bottom: 22px;
  }
  .title__rule {
    width: 360px;
    height: 10px;
    margin: 0 auto;
    background: linear-gradient(90deg, transparent, var(--gold-dark) 12%, var(--gold-dark) 88%, transparent);
    clip-path: polygon(3% 0, 100% 0, 97% 100%, 0 100%);
  }
  .title__name {
    font-weight: 600;
    font-size: 104px;
    line-height: 0.95;
    letter-spacing: 4px;
    padding: 18px 0 14px;
    text-shadow: 0 3px 0 var(--gold-dark);
  }
  .tagline {
    margin-top: 30px;
    font-family: "Barlow Condensed", sans-serif;
    font-weight: 400;
    font-size: 22px;
    letter-spacing: 0.5px;
    color: var(--gold-dark);
    text-transform: uppercase;
  }
  .band {
    position: absolute;
    left: 0;
    right: 0;
    bottom: 0;
    height: 134px;
    background: var(--band);
    display: flex;
    align-items: center;
  }
  .band__series {
    width: 170px;
    text-align: center;
    font-family: "Barlow Condensed", sans-serif;
    font-size: 24px;
    color: var(--book-ink);
  }
  .band__series strong { font-weight: 700; }
  .band__divider {
    width: 1px;
    height: 78px;
    background: var(--band-rule);
  }
  .band__author {
    flex: 1;
    text-align: center;
    font-family: "Barlow", sans-serif;
    font-weight: 700;
    font-size: 26px;
    letter-spacing: 1.5px;
    color: var(--ink);
    text-transform: uppercase;
  }
</style>
</head>
<body>
  <main class="cover">
    <div class="cover__leather" role="img" aria-label="Dark brown leather texture with soft diagonal light streaks"></div>
    <header class="title">
      <div class="title__article">THE</div>
      <div class="title__rule"></div>
      <h1 class="title__name">LANTERN<br>BUREAU</h1>
      <div class="title__rule"></div>
      <p class="tagline">Detectives, Solving Supernatural Crimes</p>
    </header>
    <footer class="band">
      <div class="band__series">BOOK <strong>#1</strong></div>
      <div class="band__divider"></div>
      <div class="band__author">Howard Blenkin Howard</div>
    </footer>
  </main>
</body>
</html>
```